Web Design for Palmwick Organic Soap Company

We need a website design for the company Velm Botanics based on the package design per attached.

The design should communicate high end, luxury organic. The site will provide facts about how the spread of disease causes deaths and can be prevented with hand washing. The site will also have a page about why we are passionate about organics and how that relates to our skin including skin facts.
Also, the site should have an e-commerce product page and shopping cart.

Target Market(s)

Educated, health conscious and socially conscious consumers who shop luxury. Target vendors include Tarrow Market and Bellquist..

Industry/Entity Type

E-Commerce

Font styles to use
Other font styles liked:
• See attached

Requirements
Must have
• Use of Ying Yang leaf Logo provided.
Based on design provided.

```html
<!DOCTYPE html>
<html lang="en">
<head>
<meta charset="utf-8">
<title>Velm Botanics – Organic Soap</title>
<link rel="stylesheet" href="https://fonts.googleapis.com/css2?family=Lato:wght@400;700&family=Raleway:wght@400;500&display=swap">
<style>
:root{
  --page:#cbc8c1;
  --panel:#ffffff;
  --ink:#2f2a25;
  --muted:#5a544d;
  --rust:#a8381f;
  --rust-dark:#8f2d18;
  --brown:#3b2a1c;
  --tan:#c8a97e;
  --paper:#c99a6b;
  --cream:#ece4d8;
  --grey:#a39f98;
  --line:#b9b5ae;
}
*{box-sizing:border-box;margin:0;padding:0}
html,body{width:890px;height:1200px;overflow:hidden}
body{background:var(--page);font-family:"Lato",Arial,sans-serif;color:var(--ink);position:relative}
.block{position:absolute;background:var(--panel)}
a{color:inherit;text-decoration:none}

/* utility bar */
.util-bar{left:58px;top:66px;width:770px;height:30px;border-bottom:1px dashed var(--line);font-size:11px;display:flex;justify-content:space-between;align-items:center;padding:0 9px}
.util-bar .links span{margin:0 3px}

/* header */
.site-header{left:58px;top:96px;width:770px;height:127px}
.brand{position:absolute;left:12px;top:28px;display:flex;align-items:center;gap:10px}
.brand-mark{width:46px;height:66px;background:var(--rust)}
.brand-name{font-family:"Raleway",sans-serif;font-size:27px;font-weight:500;color:var(--brown)}
.search{position:absolute;left:224px;top:90px;display:flex;gap:8px}
.search-input{width:256px;height:27px;background:#e9e9e9;border:1px solid #d2d2d2;font-size:11px;padding:6px 14px;color:#333}
.search-btn{width:84px;height:27px;background:var(--rust);color:#fff;font-size:11px;font-weight:700;display:flex;align-items:center;justify-content:center}
.cart{position:absolute;right:0;top:14px;width:196px;height:33px;background:var(--tan);font-size:11px;display:flex;align-items:center;padding-left:10px;gap:6px;color:var(--brown)}
.cart b{color:#fff;font-weight:700}
.assist{position:absolute;right:8px;top:62px;text-align:right}
.assist h3{font-size:13px;font-weight:700;margin-bottom:5px}
.assist .row{display:flex;justify-content:flex-end;align-items:center;gap:12px;font-size:11px}
.assist .phone{font-size:19px;margin-top:4px}

/* nav */
.main-nav{left:58px;top:238px;width:770px;height:39px;display:flex;justify-content:center;align-items:center;gap:11px}
.nav-tab{border:1px solid var(--brown);font-size:11px;padding:1px 10px;height:18px;line-height:14px}
.nav-tab.active{background:var(--brown);color:#fff}

/* hero */
.hero{position:absolute;left:58px;top:289px;width:501px;height:323px;overflow:hidden}
.hero-photo{position:absolute;inset:0;background:radial-gradient(ellipse at 40% 55%,#c9a893 0%,#9c5b4d 45%,#7a1f22 100%)}
.hero-caption{position:absolute;left:0;bottom:0;width:100%;height:59px;background:rgba(164,49,29,.9);color:#fff;font-size:20px;line-height:24px;padding:6px 14px}
.hero-arrow{position:absolute;top:145px}

.aside-video{left:570px;top:289px;width:258px;height:193px;background:var(--paper)}
.aside-title{font-family:"Raleway",sans-serif;font-size:20px;text-align:center;padding-top:8px;color:var(--ink)}
.video{position:absolute;left:18px;top:41px;width:224px;height:133px;background:#fff;padding:4px}
.video-frame{width:100%;height:100%;background:linear-gradient(135deg,#5e5c58,#a7a39d 60%,#d3d0c9)}
.aside-hygiene{left:570px;top:492px;width:258px;height:120px;background:var(--cream)}
.thumbs{position:absolute;left:16px;top:40px;display:flex;gap:13px}
.thumb{width:67px;height:61px;background:linear-gradient(160deg,#f3ecde,#d9c2a0);border:2px solid #fff}

/* top sellers */
.top-sellers{position:absolute;left:58px;top:643px;width:770px;height:213px;border:1px dashed #efece6}
.section-title{position:absolute;left:14px;top:-13px;background:var(--page);padding:0 8px;font-family:"Raleway",sans-serif;font-size:20px;color:var(--ink)}
.products{position:absolute;left:25px;top:24px;display:flex;gap:11px}
.product{width:170px;height:163px;background:#fff;border:1px solid #ddd}
.product-photo{margin:5px;height:128px}
.p1{background:linear-gradient(150deg,#e8dfcd,#f0d34a 60%,#c9ae6d)}
.p2{background:linear-gradient(150deg,#e9e2d3,#ea8a1c 55%,#b8581a)}
.p3{background:linear-gradient(150deg,#d5d0c4,#a898d9 55%,#7c9a6a)}
.p4{background:linear-gradient(150deg,#b6ad9f,#e8e0c7 55%,#9a8c76)}
.product-meta{display:flex;justify-content:space-between;align-items:center;padding:0 6px;font-size:11px}
.like{border:1px solid #9cb0d3;background:#eef2f9;font-size:9px;padding:0 4px;color:#3b5998}
.row-arrow{position:absolute;top:96px}
.view-more{position:absolute;right:28px;bottom:-7px;font-size:11px;color:var(--rust)}

/* content */
.original{left:58px;top:871px;width:528px;height:193px}
.original h2{font-family:"Raleway",sans-serif;font-weight:400;font-size:19px;color:var(--rust);text-align:center;margin-top:11px}
.original p{position:absolute;left:18px;top:53px;width:350px;font-size:11.2px;line-height:17.4px}
.stones{position:absolute;left:378px;top:48px;width:133px;height:132px;background:linear-gradient(180deg,#dcd9c5,#a9ad7c 50%,#8c9460)}
.why-shop{left:595px;top:871px;width:233px;height:193px}
.why-shop h2{font-family:"Raleway",sans-serif;font-weight:400;font-size:20px;color:var(--rust);margin:11px 0 0 11px}
.why-shop p{font-size:10.6px;line-height:14.3px;margin:10px 11px 0}
.learn-more{position:absolute;left:11px;top:166px;background:var(--brown);color:#fff;font-size:10px;padding:1px 8px}

/* newsletter */
.newsletter{left:58px;top:1081px;width:528px;height:51px}
.news-input{position:absolute;left:10px;top:13px;width:140px;height:26px;background:#e9e9e9;border:1px solid #d2d2d2;font-size:10px;padding:6px 7px;color:#666}
.news-btn{position:absolute;left:150px;top:13px;width:92px;height:26px;background:var(--rust);color:#fff;font-size:11px;font-weight:700;display:flex;align-items:center;justify-content:center}
.news-copy{position:absolute;left:252px;top:11px}
.news-copy h4{font-size:15px;font-weight:700}
.news-copy small{font-size:9.6px;font-weight:700}
.social{left:595px;top:1081px;width:233px;height:51px;background:var(--grey);display:flex;justify-content:center;align-items:center;gap:5px}
.social span{width:19px;height:19px;border-radius:50%;background:#fff}

.site-footer{position:absolute;left:0;top:1156px;width:890px;border-top:1px solid #b7b3ac;text-align:center;font-size:11px;padding-top:14px;color:var(--ink)}
</style>
</head>
<body>

<div class="block util-bar">
  <div>Why Choose Organics? / Articles / Our Blog</div>
  <div class="links">Contact Us<span>|</span>Home<span>|</span>My Account<span>|</span>Wishlist<span>|</span>Login<span>|</span>Signup</div>
</div>

<header class="block site-header">
  <div class="brand"><div class="brand-mark"></div><div class="brand-name">Velm Botanics</div></div>
  <div class="search">
    <div class="search-input">Enter product name or code</div>
    <div class="search-btn">SEARCH</div>
  </div>
  <div class="cart">20 items &nbsp;|&nbsp; $200.00
    <svg width="10" height="10" viewBox="0 0 10 10"><path d="M1 5h7M5 2l3 3-3 3" stroke="#fff" stroke-width="1.5" fill="none"/></svg>
    <b>Checkout</b>
    <svg width="16" height="14" viewBox="0 0 16 14"><path d="M1 1h3l2 8h8l2-6H5" stroke="#fff" stroke-width="1.5" fill="none"/><circle cx="7" cy="12" r="1.3" fill="#fff"/><circle cx="13" cy="12" r="1.3" fill="#fff"/></svg>
  </div>
  <div class="assist">
    <h3>Need Assistance?</h3>
    <div class="row"><svg width="18" height="11" viewBox="0 0 18 11"><rect x="1" y="1" width="16" height="9" fill="none" stroke="#555"/><path d="M1 1l8 6 8-6" fill="none" stroke="#555"/></svg>sales@velmbotanics.com</div>
    <div class="row phone"><svg width="16" height="18" viewBox="0 0 16 18"><path d="M3 1l3 3-2 3c1 3 3 5 6 6l2-2 3 3-2 3C7 17 0 10 1 3z" fill="#555"/></svg>0111 555 0182</div>
  </div>
</header>

<nav class="block main-nav">
  <span class="nav-tab active">Products</span>
  <span class="nav-tab">Natural Soaps</span>
  <span class="nav-tab">Gifts</span>
  <span class="nav-tab">Top sellers</span>
  <span class="nav-tab">For women</span>
  <span class="nav-tab">For men</span>
  <span class="nav-tab">Gift sets</span>
  <span class="nav-tab">Facial care starter sets</span>
</nav>

<section class="hero">
  <div class="hero-photo" role="img" aria-label="Hand holding an engraved oval bar of organic soap against a red background"></div>
  <svg class="hero-arrow" style="left:0" width="22" height="34" viewBox="0 0 22 34"><path d="M0 0c14 6 22 10 22 17S14 28 0 34z" fill="#fff"/><path d="M12 11l-6 6 6 6" stroke="var(--rust)" stroke-width="3" fill="none"/></svg>
  <svg class="hero-arrow" style="right:0" width="22" height="34" viewBox="0 0 22 34"><path d="M22 0C8 6 0 10 0 17s8 11 22 17z" fill="#fff"/><path d="M10 11l6 6-6 6" stroke="var(--rust)" stroke-width="3" fill="none"/></svg>
  <div class="hero-caption">We are passionate about organics and how that relates to our skin including skin facts.</div>
</section>

<aside class="block aside-video">
  <div class="aside-title">Why Use Organic Soap?</div>
  <div class="video"><div class="video-frame" role="img" aria-label="Video still of hands making soap"></div></div>
</aside>

<aside class="block aside-hygiene">
  <div class="aside-title">Hand wash &amp; Hygine</div>
  <div class="thumbs">
    <div class="thumb" role="img" aria-label="Illustration about hygiene"></div>
    <div class="thumb" role="img" aria-label="Illustration of hands being washed"></div>
    <div class="thumb" role="img" aria-label="Illustration about clean skin"></div>
  </div>
</aside>

<section class="top-sellers">
  <h2 class="section-title">Top Selling Products</h2>
  <svg class="row-arrow" style="left:8px" width="12" height="18" viewBox="0 0 12 18"><path d="M10 2L3 9l7 7" stroke="var(--rust)" stroke-width="3" fill="none"/></svg>
  <svg class="row-arrow" style="right:8px" width="12" height="18" viewBox="0 0 12 18"><path d="M2 2l7 7-7 7" stroke="var(--rust)" stroke-width="3" fill="none"/></svg>
  <div class="products">
    <div class="product"><div class="product-photo p1" role="img" aria-label="Stacked yellow soap bars tied with twine"></div><div class="product-meta"><span>$40.00</span><span class="like">Like</span></div></div>
    <div class="product"><div class="product-photo p2" role="img" aria-label="Orange soap bar with sliced orange and oil bottle"></div><div class="product-meta"><span>$40.00</span><span class="like">Like</span></div></div>
    <div class="product"><div class="product-photo p3" role="img" aria-label="Lavender and green soap bars with herbs"></div><div class="product-meta"><span>$40.00</span><span class="like">Like</span></div></div>
    <div class="product"><div class="product-photo p4" role="img" aria-label="Cream soap bar with a green leaf"></div><div class="product-meta"><span>$40.00</span><span class="like">Like</span></div></div>
  </div>
  <a class="view-more">View more products &rarr;</a>
</section>

<section class="block original">
  <h2>100% Original... natural, handmade, organic</h2>
  <p>Our pure and mild natural soaps are handmade in the old world tradition with certified organic vegetable oils, wild and organic herbs, and only pure essential oils. Neque porro quisquam est qui dolorem ipsum quia dolor sit amet, consectetur, adipisci velit,<br>Neque porro quisquam est qui dolorem ipsum quia dolor sit amet, consectetur, adipisci velitNeque porro quisquam est qui dolorem ipsum quia dolor sit amet, consectetur, adipisci velit</p>
  <div class="stones" role="img" aria-label="Stack of green natural soap bars"></div>
</section>

<section class="block why-shop">
  <h2>Why Shop With Us?</h2>
  <p>The design should communicate high-end, luxury organic. The site will provide facts about how the spread of disease causes deaths and can be prevented with hand washing. The site will also have a page about why we are passionate about organics and how that relates to our skin including skin facts. SAMPLE TEXT</p>
  <a class="learn-more">learn more</a>
</section>

<section class="block newsletter">
  <div class="news-input">reader@mailbox.example</div>
  <div class="news-btn">Get Newsletter</div>
  <div class="news-copy"><h4>Stay informed!</h4><small>We add new products frequently. SignUp for FREE newsletter</small></div>
</section>

<section class="block social" aria-label="Social links">
  <span></span><span></span><span></span><span></span><span></span><span></span>
</section>

<footer class="site-footer">Click here for legal | Media | Legal | Site Map &nbsp;/&nbsp; All rights are reserved © 2014 velmbotanics.com</footer>

</body>
</html>
```